Business Cards - Brightway Harbor

need to design unique business card for my mortgage business. I need to design credit card style business card for my business or any unique idea that you might have

Target Market(s)

Home Loan customers

Industry/Entity Type

Mortgage Brokerage

Contact Information for Business Card

please design credit card style or very unique style business card

Colors

Designer to choose colors to be used in the design.

Requirements
Must have
• Name
• position
• Phone number
• fax number
• email address
• website address
• social media address
• All above fields will be provided once design in finalised

```html
<!DOCTYPE html>
<html lang="en">
<head>
<meta charset="utf-8">
<title>Brightway Harbor – Business Cards</title>
<link rel="stylesheet" href="https://fonts.googleapis.com/css2?family=Libre+Baskerville:wght@400&family=Share+Tech+Mono&family=Courier+Prime:wght@700&display=swap">
<style>
  :root {
    --backdrop: #2b2b2e;
    --card: #ffffff;
    --card-shade: #e9ecf3;
    --blue: #2f4aa8;
    --orange: #f0891d;
    --ink: #141414;
    --title-blue: #2f4aa8;
  }
  * { box-sizing: border-box; margin: 0; padding: 0; }
  html, body { width: 1200px; height: 878px; overflow: hidden; }
  body { background: var(--backdrop); position: relative; }
  .card {
    position: absolute;
    width: 540px;
    height: 340px;
    top: 269px;
    border-radius: 22px;
    background: linear-gradient(135deg, var(--card) 0%, var(--card-shade) 55%, var(--card) 100%);
    overflow: hidden;
    box-shadow: 0 6px 18px rgba(0,0,0,0.45);
  }
  .card--front { left: 40px; }
  .card--back { left: 620px; }
  .card__sheen { position: absolute; inset: 0; width: 100%; height: 100%; }

  .brand { position: absolute; display: flex; flex-direction: column; }
  .brand__row { display: flex; align-items: center; gap: 12px; }
  .brand__name {
    font-family: "Libre Baskerville", Georgia, serif;
    color: var(--blue);
    font-weight: 400;
    line-height: 1.05;
  }
  .brand__dot { border-radius: 50%; background: var(--orange); flex: none; }
  .brand__tagline {
    font-family: "Libre Baskerville", Georgia, serif;
    color: var(--orange);
    margin-top: 6px;
  }

  .card--front .brand { left: 34px; top: 34px; }
  .card--front .brand__name { font-size: 30px; width: 180px; }
  .card--front .brand__dot { width: 22px; height: 22px; }
  .card--front .brand__tagline { font-size: 13px; }

  .address {
    position: absolute; right: 30px; top: 40px;
    text-align: right;
    font-family: "Courier Prime", "Courier New", monospace;
    font-weight: 700; font-size: 12.5px; line-height: 1.55;
    color: var(--ink);
  }
  .address__gap { height: 10px; }

  .phones {
    position: absolute; left: 34px; top: 172px;
    font-family: "Share Tech Mono", monospace;
    font-size: 16px; letter-spacing: 0.5px;
    color: var(--ink);
    white-space: nowrap;
  }
  .phones span + span { margin-left: 12px; }

  .person { position: absolute; left: 34px; top: 222px; }
  .person__name {
    font-family: "Courier Prime", "Courier New", monospace;
    font-weight: 700; font-size: 20px; letter-spacing: 9px;
    color: var(--ink);
  }
  .person__title {
    font-family: "Courier Prime", "Courier New", monospace;
    font-weight: 700; font-size: 11px; letter-spacing: 6px;
    color: var(--title-blue);
    margin-top: 4px;
  }

  .social { position: absolute; right: 34px; bottom: 30px; display: flex; gap: 12px; }
  .social__item { width: 30px; height: 30px; border-radius: 50%; background: var(--orange); }

  .card--back .brand { left: 230px; top: 76px; }
  .card--back .brand__name { font-size: 34px; width: 200px; }
  .card--back .brand__dot { width: 26px; height: 26px; }
  .card--back .brand__tagline { font-size: 14px; }

  .web-band {
    position: absolute; left: 0; right: 0; top: 226px; height: 34px;
    background: var(--blue);
    display: flex; align-items: center; padding-left: 40px;
    font-family: "Courier Prime", "Courier New", monospace;
    font-weight: 700; font-size: 13px; letter-spacing: 6px;
    color: #ffffff;
    white-space: nowrap;
  }
</style>
</head>
<body>

  <section class="card card--front">
    <svg class="card__sheen" viewBox="0 0 540 340" aria-hidden="true">
      <path d="M120 0 C200 120 260 220 300 340" fill="none" stroke="#ffffff" stroke-width="26" opacity="0.7"/>
      <path d="M330 0 C380 140 420 240 470 340" fill="none" stroke="#dde2ec" stroke-width="18" opacity="0.6"/>
    </svg>

    <div class="brand">
      <div class="brand__row">
        <div class="brand__name">Brightway Harbor</div>
        <span class="brand__dot"></span>
      </div>
      <div class="brand__tagline">Steady keys, Open doors</div>
    </div>

    <div class="address">
      <div>Suite 410, 18 Marlow Street</div>
      <div>Castle Hill NSW 2154</div>
      <div class="address__gap"></div>
      <div>daniel@brightwayharbor.com</div>
      <div>www.brightwayharbor.com</div>
    </div>

    <div class="phones">
      <span>P:27 10 555 0148</span><span>M:27 34 555 0392</span><span>F:27 82 555 0716</span>
    </div>

    <div class="person">
      <div class="person__name">DANIEL REEVES</div>
      <div class="person__title">MANAGING DIRECTOR</div>
    </div>

    <div class="social">
      <span class="social__item"></span>
      <span class="social__item"></span>
      <span class="social__item"></span>
      <span class="social__item"></span>
      <span class="social__item"></span>
    </div>
  </section>

  <section class="card card--back">
    <svg class="card__sheen" viewBox="0 0 540 340" aria-hidden="true">
      <path d="M90 0 C170 130 230 230 260 340" fill="none" stroke="#ffffff" stroke-width="26" opacity="0.7"/>
      <path d="M360 0 C400 140 440 240 500 340" fill="none" stroke="#dde2ec" stroke-width="18" opacity="0.6"/>
    </svg>

    <div class="brand">
      <div class="brand__row">
        <div class="brand__name">Brightway Harbor</div>
        <span class="brand__dot"></span>
      </div>
      <div class="brand__tagline">Steady keys, Open doors</div>
    </div>

    <div class="web-band">WWW.BRIGHTWAYHARBOR.COM</div>
  </section>

</body>
</html>
```